arts & crafts

I collect old plates & make them into serving plates for cakes, afternoon teas, special occasions, weddings, parties, bridal showers. cake competitions, displays in bakeries.

Contact Information for Business Card

Tulips Turn Gold
Bringing the old back to new
Ph 0412873905
info@ tulipsturngold.com.au
www.tulipsturngold.com.au
facebook
Craftly

```html
<!DOCTYPE html>
<html lang="en">
<head>
<meta charset="utf-8">
<title>Tulips Turn Gold – Business Card</title>
<link rel="stylesheet" href="https://fonts.googleapis.com/css2?family=Pinyon+Script&family=Gabriela&display=swap">
<style>
  :root {
    --backdrop: #ededed;
    --card-blue: #6a7fbf;
    --band-white: #ffffff;
    --ink-navy: #2c2b7c;
    --ring-blue: #3b3f9a;
    --text-white: #ffffff;
  }
  html, body {
    margin: 0;
    width: 1200px;
    height: 898px;
    overflow: hidden;
    background: var(--backdrop);
  }
  .canvas {
    position: relative;
    width: 1200px;
    height: 898px;
  }
  .card {
    position: absolute;
    left: 50px;
    top: 109px;
    width: 1100px;
    height: 680px;
    border-radius: 56px;
    background: var(--card-blue);
    overflow: hidden;
    font-family: "Gabriela", Georgia, serif;
  }
  .tagline {
    position: absolute;
    top: 34px;
    left: 0;
    width: 100%;
    margin: 0;
    text-align: center;
    font-family: "Pinyon Script", cursive;
    font-weight: 400;
    font-size: 60px;
    color: var(--text-white);
    line-height: 1.2;
  }
  .info-band {
    position: absolute;
    top: 251px;
    left: 0;
    width: 100%;
    height: 207px;
    background: var(--band-white);
  }
  .band-item {
    position: absolute;
    top: 310px;
    height: 70px;
    display: flex;
    align-items: center;
    color: var(--ink-navy);
    font-size: 27px;
    line-height: 1;
    white-space: nowrap;
  }
  .shop-phone { left: 54px; gap: 6px; }
  .shop-name { margin-right: 4px; }
  .social { left: 736px; gap: 14px; }
  .social-dot {
    width: 64px;
    height: 64px;
    border-radius: 50%;
    background: var(--card-blue);
  }
  .badge {
    position: absolute;
    left: 372px;
    top: 158px;
    width: 356px;
    height: 356px;
  }
  .badge-ring {
    position: absolute;
    inset: 0;
    width: 100%;
    height: 100%;
  }
  .badge-name {
    position: absolute;
    inset: 0;
    display: flex;
    align-items: center;
    justify-content: center;
    text-align: center;
    color: var(--ink-navy);
    font-size: 40px;
    line-height: 1.15;
  }
  .contact-row {
    position: absolute;
    top: 576px;
    left: 62px;
    display: flex;
    align-items: center;
    color: var(--text-white);
    font-size: 30px;
    line-height: 1;
    white-space: nowrap;
  }
  .contact-row .icon { margin-right: 12px; }
  .contact-row .web { margin-left: 24px; }
</style>
</head>
<body>
<div class="canvas">
  <section class="card" aria-label="Tulips Turn Gold business card">
    <h1 class="tagline">Bringing the old back to new</h1>

    <div class="info-band"></div>

    <div class="band-item shop-phone">
      <span class="shop-name">Craftly</span>
      <svg class="icon" width="26" height="30" viewBox="0 0 24 24" aria-hidden="true">
        <path fill="#6a7fbf" d="M6.6 10.8c1.4 2.8 3.8 5.1 6.6 6.6l2.2-2.2c.3-.3.7-.4 1-.2 1.1.4 2.3.6 3.6.6.6 0 1 .4 1 1V20c0 .6-.4 1-1 1C10.6 21 3 13.4 3 4c0-.6.4-1 1-1h3.5c.6 0 1 .4 1 1 0 1.3.2 2.5.6 3.6.1.3 0 .7-.2 1L6.6 10.8z"/>
      </svg>
      <span class="phone">0412873905</span>
    </div>

    <div class="badge">
      <svg class="badge-ring" viewBox="0 0 356 356" aria-hidden="true">
        <circle cx="178" cy="178" r="177" fill="#ffffff"/>
        <circle cx="178" cy="178" r="146" fill="none" stroke="#3b3f9a" stroke-width="3"/>
        <circle cx="178" cy="178" r="136" fill="none" stroke="#3b3f9a" stroke-width="1.5"/>
      </svg>
      <div class="badge-name">Tulips<br>Turn<br>Gold</div>
    </div>

    <div class="band-item social">
      <span class="social-dot" aria-hidden="true"></span>
      <span class="social-name">Tulips Turn Gold</span>
    </div>

    <div class="contact-row">
      <svg class="icon" width="44" height="30" viewBox="0 0 44 30" aria-hidden="true">
        <rect x="2" y="2" width="40" height="26" fill="none" stroke="#fff" stroke-width="3"/>
        <polyline points="2,2 22,18 42,2" fill="none" stroke="#fff" stroke-width="3"/>
      </svg>
      <span class="email">info@ tulipsturngold.com.au</span>
      <svg class="icon web" width="40" height="40" viewBox="0 0 40 40" aria-hidden="true">
        <g fill="none" stroke="#fff" stroke-width="2.5">
          <circle cx="20" cy="20" r="17"/>
          <ellipse cx="20" cy="20" rx="8" ry="17"/>
          <line x1="3" y1="20" x2="37" y2="20"/>
          <line x1="20" y1="3" x2="20" y2="37"/>
        </g>
      </svg>
      <span class="website">www.tulipsturngold.com.au</span>
    </div>
  </section>
</div>
</body>
</html>
```